Postcard Handout

We need a postcard to market university fairs in Southeast Asia. The fairs are organized by ScholarBridge which is a program of the Federal Bureau of Outreach http://lrn.outreachbureau.example/scholarbridge/

The audience for these postcards are U.S. higher education recruiters (not students). We want U.S. universities to sign up for the fairs.

The postcards will be handed out at large education conferences.

Target Market(s)

U.S. university recruiters who are between the ages of 25 and 45.

Industry/Entity Type

University

Requirements
Must have

• Copy/Text: Please see attached doc. file for copy/text to be used on the front and back of the card.

Front: High color gloss

Back: Black and white only design

Featured Colors: Red, White, and Blue
- Should have a patriotic / U.S. government feel

Logos: Must use the Outreach Bureau logo and at least one ScholarBridge logo (can use more but not required)
Nice to have
• -

```html
<!DOCTYPE html>
<html lang="en">
<head>
<meta charset="utf-8">
<title>2015 Southeast Asia Fair Series Postcard</title>
<link href="https://fonts.googleapis.com/css2?family=Oswald:wght@500;600&family=Open+Sans:wght@400;600;700&display=swap" rel="stylesheet">
<style>
:root{
  --navy:#23406e;
  --red:#b5213a;
  --pink:#f8d9de;
  --cell-pink:#efc9c5;
  --sea:#8fd0ec;
  --land:#8cc63f;
  --stage:#2b2b2b;
  --white:#ffffff;
  --ink:#111111;
}
*{box-sizing:border-box;margin:0;padding:0}
html,body{width:1200px;height:1000px;overflow:hidden}
body{background:var(--stage);position:relative;font-family:"Open Sans",Arial,sans-serif}

/* Front */
.card-front{position:absolute;left:7px;top:8px;width:655px;height:506px;background:var(--white);overflow:hidden}
.front-title{position:absolute;left:0;right:0;top:14px;text-align:center;font-family:"Oswald",Impact,sans-serif;font-weight:600;font-size:28px;color:var(--red);letter-spacing:.1px;white-space:nowrap}
.rule{position:absolute;left:0;right:0;height:10px;border-top:3px solid var(--navy);border-bottom:3px solid var(--red)}
.rule-top{top:56px}
.rule-bottom{top:424px}
.region-map{position:absolute;left:0;right:0;top:66px;height:358px;background:linear-gradient(135deg,var(--land) 0%,var(--land) 38%,var(--sea) 55%,var(--sea) 100%)}
.date-badge{position:absolute;left:507px;top:64px;width:130px;height:130px;border-radius:50%;background:var(--navy);display:flex;align-items:center;justify-content:center}
.date-badge-inner{width:104px;height:104px;border-radius:50%;background:var(--red);border:2px dotted var(--white);color:var(--white);font-family:"Oswald",Impact,sans-serif;font-weight:600;font-size:15px;line-height:1.3;text-align:center;display:flex;flex-direction:column;justify-content:center}
.front-footer{position:absolute;left:0;right:0;top:436px;height:70px}
.org-mark{position:absolute;top:12px;display:flex;align-items:center;gap:5px;font-size:10px;font-weight:600;color:var(--navy)}
.org-mark .dot{width:22px;height:22px;border-radius:50%;background:var(--navy);flex:none}
.org-bureau{left:10px;width:90px}
.org-program{left:104px;width:88px;color:var(--red)}
.org-program .dot{background:var(--red)}
.divider{position:absolute;left:196px;top:8px;width:1px;height:54px;background:#ccc}
.subscribe{position:absolute;right:18px;top:10px;text-align:right;white-space:nowrap}
.subscribe-line{font-size:19px;color:var(--navy)}
.subscribe-link{font-size:19px;font-weight:700;color:var(--red)}

/* Back */
.card-back{position:absolute;left:575px;top:518px;width:613px;height:474px;background:var(--pink);overflow:hidden}
.zone-white{position:absolute;background:var(--white)}
.zone-cal{left:0;top:0;width:470px;height:150px}
.zone-list{left:0;top:150px;width:300px;height:252px}
.zone-corner{left:0;top:402px;width:70px;height:72px}
.zone-label{position:absolute;font-size:17px;color:var(--ink);text-align:center}
.calendar{position:absolute;left:27px;top:8px;border-collapse:collapse;color:var(--navy)}
.calendar th{font-weight:400;font-size:16px;height:22px;border:1px solid var(--navy);text-align:center}
.calendar th.sun{color:var(--red)}
.calendar td{border:1px solid var(--navy);height:38px;font-size:16px;text-align:center;position:relative;padding-right:10px}
.calendar tr.feb-row td{border-top:3px solid var(--navy);height:36px}
.calendar td.sun{background:var(--cell-pink);color:var(--red)}
.num{display:inline-flex;align-items:center;justify-content:center;width:15px;height:15px;border-radius:50%;background:var(--navy);color:var(--white);font-size:8px;font-weight:700;border:1px solid var(--red);vertical-align:-6px;margin-left:1px;flex:none}
.month{position:absolute;left:4px;font-size:15px;color:var(--navy);transform:rotate(-90deg);transform-origin:center}
.count-badge{position:absolute;left:222px;top:125px;width:78px;height:78px;border-radius:50%;background:var(--navy);display:flex;align-items:center;justify-content:center}
.count-badge span{width:60px;height:60px;border-radius:50%;background:var(--red);border:1px dotted var(--white);color:var(--white);font-family:"Oswald",Impact,sans-serif;font-size:9px;line-height:1.2;display:flex;align-items:center;justify-content:center;text-align:center}
.save-head{position:absolute;left:22px;top:162px;font-family:"Oswald",Impact,sans-serif;font-weight:600;font-size:14px;color:var(--red)}
.venue-list{position:absolute;top:204px;list-style:none;font-size:12px;color:var(--navy);font-weight:600;width:146px}
.venue-list li{height:20.3px;display:flex;align-items:center;gap:3px;white-space:nowrap;letter-spacing:-.1px}
.venue-list .num{margin-left:0;vertical-align:0}
.venue-list small{font-size:6px;font-weight:400;margin-left:2px}
.venue-a{left:8px}
.venue-b{left:158px}
.contact{position:absolute;left:18px;top:354px;font-family:"Oswald",Impact,sans-serif;font-weight:600;font-size:15px;line-height:1.25;color:var(--red);white-space:nowrap}
</style>
</head>
<body>

<section class="card-front">
  <h1 class="front-title">Join us for the 2015 Southeast Asia Fair Series</h1>
  <div class="rule rule-top"></div>
  <div class="region-map" role="img" aria-label="Map of Southeast Asia with pins marking Burma, Thailand, Cambodia, Vietnam, Malaysia and Brunei"></div>
  <div class="date-badge"><div class="date-badge-inner"><span>January 21</span><span>–</span><span>February 3</span></div></div>
  <div class="rule rule-bottom"></div>
  <footer class="front-footer">
    <div class="org-mark org-bureau"><span class="dot"></span>Federal Bureau of Outreach</div>
    <div class="org-mark org-program"><span class="dot"></span>ScholarBridge</div>
    <div class="divider"></div>
    <div class="subscribe">
      <div class="subscribe-line">Subscribe to our newsletter to receive updates</div>
      <div class="subscribe-link">lnk.example/FairUpdates</div>
    </div>
  </footer>
</section>

<section class="card-back">
  <div class="zone-white zone-cal"></div>
  <div class="zone-white zone-list"></div>
  <div class="zone-white zone-corner"></div>

  <span class="zone-label" style="left:490px;top:58px;width:110px;line-height:1.3">Postage<br>Area</span>
  <span class="zone-label" style="left:380px;top:188px;width:160px">Address Area</span>
  <span class="zone-label" style="left:270px;top:430px;width:160px">Barcode Area</span>

  <span class="month" style="top:52px">Jan</span>
  <span class="month" style="top:122px">Feb</span>

  <table class="calendar">
    <tr><th class="sun" style="width:61px">Sun</th><th style="width:57px">Mon</th><th style="width:66px">Tue</th><th style="width:65px">Wed</th><th style="width:66px">Thu</th><th style="width:66px">Fri</th><th style="width:57px">Sat</th></tr>
    <tr><td class="sun"></td><td></td><td></td><td>21<span class="num">1</span></td><td>22<span class="num">2</span></td><td>23<span class="num">3</span></td><td>24<span class="num">4</span></td></tr>
    <tr><td class="sun">25<span class="num">5</span></td><td>26<span class="num">6</span></td><td>27<span class="num">7</span></td><td>28<span class="num">8</span></td><td>29<span class="num">9</span></td><td>30<span class="num">10</span></td><td>31<span class="num">11</span></td></tr>
    <tr class="feb-row"><td class="sun">1<span class="num">12</span></td><td>2<span class="num">13</span></td><td>3<span class="num">14</span></td><td></td><td></td><td></td><td></td></tr>
  </table>

  <div class="count-badge"><span>10 Cities/<br>6 Countries</span></div>

  <h2 class="save-head">Save the dates!</h2>
  <ul class="venue-list venue-a">
    <li><span class="num">1</span>Mandalay</li>
    <li><span class="num">2</span>Yangon</li>
    <li><span class="num">3</span>Chiang Mai</li>
    <li><span class="num">4</span>Bangkok</li>
    <li><span class="num">5</span>Kuala Lumpur</li>
    <li><span class="num">6</span>Kuala Lumpur /<small>Penang travel</small></li>
    <li><span class="num">7</span>Penang</li>
  </ul>
  <ul class="venue-list venue-b">
    <li><span class="num">8</span>Penang /<small>HCMC travel</small></li>
    <li><span class="num">9</span>Ho Chi Minh City</li>
    <li><span class="num">10</span>Hanoi</li>
    <li><span class="num">11</span>Hanoi /<small>Phnom Penh travel</small></li>
    <li><span class="num">12</span>Phnom Penh</li>
    <li><span class="num">13</span>Phnom Penh /<small>Brunei travel</small></li>
    <li><span class="num">14</span>Brunei</li>
  </ul>

  <p class="contact">Questions?<br>Email SEAsiaFairs@scholarbridge.example</p>
</section>

</body>
</html>
```